Concrete Construction Business Card design

We are a commercial concrete construction company based in Texas. a family owned business which our trade was passed down and taught by our grandfather whom we want represented in this design. our grandfathers nick name was "pepe" so we are wanting the letter G to be symbolized in some way with a red pepe . colors should be possibly a grey color back ground , green letter g and red pepe pepper , to be left for you to decide with integrity , concrete professionalism,and mexican heritage

Target Market(s)

general contractors, architects,inverstors, and engineers

Industry/Entity Type

Concrete

Contact Information for Business Card

Herrera Concrete Construction LLC, Dennis Herrera, 1872 Bramblewood Ln. Brenly, TX 76481, (940)318-2746, dhslabworkllc48@quarrymail.net

```html
<!DOCTYPE html>
<html lang="en">
<head>
<meta charset="UTF-8">
<title>Herrera Concrete Construction LLC – Business Card</title>
<link rel="stylesheet" href="https://fonts.googleapis.com/css2?family=Roboto:wght@400;700&family=Source+Sans+3:wght@400;600&display=swap">
<style>
  :root {
    --page-bg: #000000;
    --slate-light: #5e646b;
    --slate-dark: #2e3235;
    --accent-green: #b9d873;
    --field-green-light: #c1da78;
    --field-green-dark: #a2b760;
    --band-sage: #879478;
    --ink: #474a4d;
    --ring: #8d9486;
  }
  * { margin: 0; padding: 0; box-sizing: border-box; }
  html, body {
    width: 1200px;
    height: 1200px;
    overflow: hidden;
    background: var(--page-bg);
  }
  .business-card {
    position: absolute;
    left: 192px;
    top: 351px;
    width: 867px;
    height: 495px;
    overflow: hidden;
    background: radial-gradient(ellipse 70% 90% at 50% 20%, var(--slate-light), var(--slate-dark));
  }
  .card-waves {
    position: absolute;
    inset: 0;
    width: 100%;
    height: 100%;
  }
  .brand-mark {
    position: absolute;
    left: 43px;
    top: 43px;
    width: 142px;
    height: 142px;
    border-radius: 50%;
    border: 3px solid var(--ring);
    padding: 8px;
  }
  .brand-mark span {
    display: block;
    width: 100%;
    height: 100%;
    border-radius: 50%;
    background: var(--accent-green);
  }
  .company-name {
    position: absolute;
    left: 212px;
    top: 84px;
    font-family: "Roboto", sans-serif;
    font-weight: 700;
    font-size: 34px;
    color: var(--accent-green);
    white-space: nowrap;
  }
  .company-address {
    position: absolute;
    left: 252px;
    top: 143px;
    font-family: "Roboto", sans-serif;
    font-weight: 400;
    font-size: 28px;
    color: var(--accent-green);
    white-space: nowrap;
  }
  .contact {
    position: absolute;
    left: 42px;
    top: 333px;
    font-family: "Source Sans 3", sans-serif;
    color: var(--ink);
  }
  .contact-name {
    font-weight: 600;
    font-size: 45px;
    line-height: 54px;
  }
  .contact-line {
    font-weight: 400;
    font-size: 30px;
    line-height: 41px;
  }
</style>
</head>
<body>
  <div class="business-card">
    <svg class="card-waves" viewBox="0 0 867 495" preserveAspectRatio="none" aria-hidden="true">
      <defs>
        <linearGradient id="field-green" x1="0" y1="0" x2="1" y2="0">
          <stop offset="0" stop-color="var(--field-green-light)"/>
          <stop offset="1" stop-color="var(--field-green-dark)"/>
        </linearGradient>
      </defs>
      <path class="sage-band" d="M0,164 C120,270 300,300 500,303 C680,306 800,330 867,382 L867,495 L0,495 Z" fill="var(--band-sage)"/>
      <path class="green-field" d="M0,222 C130,320 320,328 500,332 C680,336 800,352 867,406 L867,495 L0,495 Z" fill="url(#field-green)"/>
    </svg>

    <div class="brand-mark" aria-hidden="true"><span></span></div>
    <div class="company-name">Herrera Concrete Construction LLC</div>
    <div class="company-address">1872 Bramblewood Ln. Brenly, TX 76481</div>

    <div class="contact">
      <div class="contact-name">Dennis Herrera</div>
      <div class="contact-line">(940)318-2746</div>
      <div class="contact-line">dhslabworkllc48@quarrymail.net</div>
    </div>
  </div>
</body>
</html>
```